Business Card Design Project

Name of Company: Halvorine Coaching & Consulting
Possible Acronym: HC&C
My Name: Mirabel Halvorine, LL.B.
My email address: mirabel@halvorineconsulting.example
My tel.: +44 (0) 7938 604 275
My skype address: halvorinehc
I am offering executive coaching and consulting in the area of business development and strategic planning to intellectual property law firms around the world.
Since I will be marketing to the legal industry, the card must be fairly conservative. However I want it to also have flare and spark. I want to convey to potential clients that I can be the spark that will ignite their potential. I like the combination of navy blue and hot pink. However, I have decided that hot pink is not corporate enough so I would like to use a colour with navy that comes close to hot pink but is more conservative. Not red. I would consider swapping navy blue for grey if you thought that would look better. I would like the background of the card to be entirely white - both back and front - only the letters will be in colour.
I would like the card to be double sided with the name of my firm (or the acronym) and my email address underneath (mirabel@halvorineconsulting.example) on the back and on the front, all of the information above.
With gratitude!
Mirabel

```html
<!DOCTYPE html>
<html lang="en">
<head>
<meta charset="utf-8">
<title>Halvorine Coaching &amp; Consulting — Business Card</title>
<link rel="stylesheet" href="https://fonts.googleapis.com/css2?family=Cinzel:wght@500&family=Open+Sans:wght@400;700&display=swap">
<style>
  :root {
    --navy: #1b3264;
    --plum: #a0317c;
    --paper: #f3f3f3;
    --page: #ffffff;
    --ink-grey: #5e5e5e;
    --mist: #dcdcdc;
  }
  * { box-sizing: border-box; margin: 0; padding: 0; }
  html, body { width: 1200px; height: 894px; overflow: hidden; background: var(--page); }
  .canvas { position: relative; width: 1200px; height: 894px; }

  .card {
    position: absolute;
    top: 302px;
    width: 505px;
    height: 290px;
    background: var(--paper);
    overflow: hidden;
    box-shadow: 0 0 0 1px #e4e4e4;
  }
  .card--front { left: 70px; }
  .card--back  { left: 625px; }

  .brand { position: absolute; display: flex; align-items: center; gap: 10px; color: var(--navy); }
  .brand__mark { width: 56px; height: 44px; background: var(--navy); flex: none; }
  .brand__name { font-family: "Cinzel", Georgia, serif; font-weight: 500; line-height: 1.05; }
  .brand__name .line1 { display: block; font-size: 21px; letter-spacing: 0.5px; }
  .brand__name .line2 { display: block; font-size: 9.5px; letter-spacing: 0.3px; }

  .card--front .brand { left: 17px; top: 17px; }

  .card--back .brand { left: 60px; top: 58px; gap: 14px; }
  .card--back .brand__mark { width: 74px; height: 58px; }
  .card--back .brand__name .line1 { font-size: 28px; }
  .card--back .brand__name .line2 { font-size: 12.5px; }

  .splash {
    position: absolute;
    top: 0; right: 0;
    width: 175px; height: 100%;
  }
  .splash--plum { background: radial-gradient(ellipse at 60% 62%, var(--plum) 0%, var(--plum) 38%, rgba(160,49,124,0) 72%); }
  .splash--mist { width: 230px; background: radial-gradient(ellipse at 62% 70%, var(--mist) 0%, var(--mist) 32%, rgba(220,220,220,0) 70%); }

  .holder {
    position: absolute; left: 17px; top: 145px;
    font-family: "Open Sans", Arial, sans-serif; font-weight: 700;
    font-size: 14px; color: var(--navy); text-transform: uppercase;
  }
  .contacts { position: absolute; left: 17px; top: 172px; list-style: none; }
  .contact {
    display: flex; align-items: center; gap: 7px;
    font-family: "Open Sans", Arial, sans-serif; font-size: 11px;
    color: var(--ink-grey); height: 16.5px;
  }
  .contact svg { width: 10px; height: 10px; fill: var(--plum); flex: none; }

  .card--back .contact { position: absolute; left: 60px; top: 150px; font-size: 12px; }
</style>
</head>
<body>
<main class="canvas">

  <section class="card card--front" aria-label="Card front">
    <div class="splash splash--plum" role="img" aria-label="Plum paint splash decoration"></div>
    <div class="brand">
      <span class="brand__mark"></span>
      <span class="brand__name"><span class="line1">HALVORINE</span><span class="line2">COACHING &amp; CONSULTING</span></span>
    </div>
    <p class="holder">Mirabel Halvorine, LL.B.</p>
    <ul class="contacts">
      <li class="contact">
        <svg viewBox="0 0 10 10" aria-hidden="true"><path d="M2 0.5 L3.6 0.5 L4.2 3 L3 3.8 Q4 6.2 6.2 7 L7 5.8 L9.5 6.4 L9.5 8 Q9.5 9.5 8 9.5 Q1 9 0.5 2 Q0.5 0.5 2 0.5Z"/></svg>
        +44 (0) 7938 604 275
      </li>
      <li class="contact">
        <svg viewBox="0 0 10 10" aria-hidden="true"><path d="M0.5 2 H9.5 V8.5 H0.5Z M1.3 2.8 L5 5.6 L8.7 2.8" fill="none" stroke="#a0317c" stroke-width="1.2"/></svg>
        mirabel@halvorineconsulting.example
      </li>
      <li class="contact">
        <svg viewBox="0 0 10 10" aria-hidden="true"><circle cx="5" cy="5" r="4.5"/></svg>
        halvorinehc
      </li>
    </ul>
  </section>

  <section class="card card--back" aria-label="Card back">
    <div class="splash splash--mist" role="img" aria-label="Faint grey paint splash decoration"></div>
    <div class="brand">
      <span class="brand__mark"></span>
      <span class="brand__name"><span class="line1">HALVORINE</span><span class="line2">COACHING &amp; CONSULTING</span></span>
    </div>
    <p class="contact">
      <svg viewBox="0 0 10 10" aria-hidden="true"><path d="M0.5 2 H9.5 V8.5 H0.5Z M1.3 2.8 L5 5.6 L8.7 2.8" fill="none" stroke="#a0317c" stroke-width="1.2"/></svg>
      mirabel@halvorineconsulting.example
    </p>
  </section>

</main>
</body>
</html>
```